Business Card Design Project

I require a business card with the following information on them for various different people;
name
m:
f:
e:
I have a logo already and will attached that. We are in the construction industry. I require something clean and simple but eye catching at the same time. You can use another colour with our logo if you like and you can style the logo as well if you wish. I am open.
Also it needs to be front and back design.
Industry/Entity Type
Construction
Requirements
Must have
- Logo, name, mobile, fax and email address.
Front and back design

```html
<!DOCTYPE html>
<html lang="en">
<head>
<meta charset="utf-8">
<title>Oakbrook Developments – Business Card</title>
<link rel="stylesheet" href="https://fonts.googleapis.com/css2?family=Arimo:wght@400&display=swap">
<style>
  :root {
    --bg-top: #ffffff;
    --bg-bottom: #d8dcdc;
    --card-white: #ffffff;
    --brand-green: #7cc51c;
    --lime-top: #b3f02a;
    --lime-bottom: #92de12;
    --ink-grey: #555b5e;
    --paper-white: #ffffff;
  }
  * { margin: 0; padding: 0; box-sizing: border-box; }
  html, body {
    width: 1200px;
    height: 1200px;
    overflow: hidden;
  }
  body {
    position: relative;
    background: linear-gradient(to bottom, var(--bg-top) 0%, var(--bg-top) 12%, var(--bg-bottom) 100%);
    font-family: "Arimo", Arial, sans-serif;
  }
  .card {
    position: absolute;
  }
  .card-front {
    left: 248px;
    top: 190px;
    width: 700px;
    height: 390px;
    background: var(--card-white);
    text-align: center;
  }
  .brand-lockup {
    position: absolute;
    left: 30px;
    right: 30px;
    top: 42px;
    display: flex;
    align-items: center;
    justify-content: center;
    gap: 18px;
  }
  .brand-square {
    width: 42px;
    height: 42px;
    background: var(--brand-green);
    border-radius: 6px;
  }
  .brand-name {
    font-size: 50px;
    color: var(--ink-grey);
    letter-spacing: 0.5px;
    line-height: 1;
  }
  .brand-rule {
    position: absolute;
    left: 24px;
    top: 148px;
    width: 600px;
    height: 4px;
  }
  .person-name {
    position: absolute;
    left: 0;
    right: 0;
    top: 168px;
    font-size: 28px;
    color: var(--brand-green);
  }
  .contact-line {
    position: absolute;
    left: 0;
    right: 0;
    font-size: 23px;
    color: var(--ink-grey);
  }
  .contact-line .label { color: var(--brand-green); }
  .contact-mobile { top: 228px; }
  .contact-fax { top: 284px; }
  .contact-email { top: 340px; font-size: 24px; }
  .card-back {
    left: 249px;
    top: 668px;
    width: 702px;
    height: 402px;
    background: linear-gradient(to bottom, var(--lime-top), var(--lime-bottom));
  }
  .back-brand {
    position: absolute;
    left: 52px;
    bottom: 52px;
    display: flex;
    align-items: center;
    gap: 16px;
  }
  .back-brand .brand-square { background: var(--paper-white); }
  .back-brand .brand-name { color: var(--paper-white); font-size: 44px; }
</style>
</head>
<body>
  <section class="card card-front">
    <div class="brand-lockup">
      <span class="brand-square"></span>
      <span class="brand-name">Oakbrook Developments</span>
    </div>
    <svg class="brand-rule" viewBox="0 0 600 4" preserveAspectRatio="none" aria-hidden="true">
      <defs>
        <linearGradient id="ruleFade" x1="0" x2="1" y1="0" y2="0">
          <stop offset="0" stop-color="#7cc51c"/>
          <stop offset="0.7" stop-color="#b7e07a"/>
          <stop offset="1" stop-color="#ffffff"/>
        </linearGradient>
      </defs>
      <rect x="0" y="0" width="600" height="4" fill="url(#ruleFade)"/>
    </svg>
    <p class="person-name">John Smith</p>
    <p class="contact-line contact-mobile"><span class="label">M:</span> 555.555.5555</p>
    <p class="contact-line contact-fax"><span class="label">F:</span> 555.555.5556</p>
    <p class="contact-line contact-email">JohnSmith@OakbrookDevelopments.com</p>
  </section>

  <section class="card card-back">
    <div class="back-brand">
      <span class="brand-square"></span>
      <span class="brand-name">Oakbrook Developments</span>
    </div>
  </section>
</body>
</html>
```